Design a Website Mockup for Reel Tide Rovers

We need a mockup design done for our homepage and lake page. The winner of this contest would also be used to design the rest of our site, as well as possibly a mobile site and app. The look and feel should match our logo and should be targeted at anglers who are mostly male and between 18-55 years of age. Attached are the logo and the requirements for each page.

The design should be completely unique and modern but easy to use.

Expected Deliverables:

.psd and jpeg/png of the Homepage Design
.psd and jpeg/png of the Lake Page Design

```html
<!DOCTYPE html>
<html lang="en">
<head>
<meta charset="utf-8">
<title>Reel Tide Rovers — Home</title>
<link href="https://fonts.googleapis.com/css2?family=Open+Sans:ital,wght@0,400;0,600;0,700;1,400&display=swap" rel="stylesheet">
<style>
:root{
  --red:#c8161d;
  --dark:#3a3a3a;
  --darker:#2e2e2e;
  --ink:#222;
  --muted:#555;
  --page:#f7f7f7;
  --rule:#c9c9c9;
  --white:#fff;
}
*{box-sizing:border-box;margin:0;padding:0}
html,body{width:714px;height:1200px;overflow:hidden}
body{position:relative;background:var(--page);font-family:"Open Sans",Arial,sans-serif;color:var(--ink)}
.abs{position:absolute}
a{color:inherit;text-decoration:none}

/* header */
.brand{left:148px;top:20px;display:flex;align-items:center;gap:8px}
.brand-dot{width:34px;height:34px;border-radius:50%;background:var(--red)}
.brand-name{font-size:19px;font-weight:700;color:var(--red);letter-spacing:.5px}
.social-top{right:18px;top:6px;display:flex;gap:6px}
.social-top span{width:10px;height:10px;background:#2f5d9a;border-radius:2px}
.social-top .badge{width:36px;background:#dde3ee;border:1px solid #b9c3d6}
.account{right:18px;top:25px;font-size:7.5px;color:#333;word-spacing:2px}
.search{right:18px;top:44px;display:flex;gap:12px}
.search div{height:12px;border:1px solid #999;border-radius:2px;background:#fff;font-size:5.5px;color:#555;display:flex;align-items:center;justify-content:center;position:relative}
.search div::after{content:"";position:absolute;right:3px;top:4px;border:3px solid transparent;border-top-color:#333}

.nav{left:0;top:70px;width:714px;height:20px;background:var(--dark);display:flex;justify-content:center;gap:24px;padding-left:40px}
.nav a{color:#fff;font-size:8.5px;line-height:20px}

/* slider */
.slide{top:96px;height:183px}
.s-left{left:0;width:177px;background:linear-gradient(#c9813a,#8a4a15)}
.s-main{left:179px;width:361px;background:linear-gradient(#4f6f9c 0%,#b9c4d0 40%,#2c3e63 60%,#13213f)}
.s-right{left:542px;width:172px;background:linear-gradient(#4a3410,#c98a1f 45%,#2a1d08)}
.arrow{top:173px;width:28px;height:28px;border-radius:50%;background:rgba(200,200,200,.7);display:flex;align-items:center;justify-content:center}

/* welcome */
.welcome{left:137px;top:283px;font-size:22px;font-style:italic;color:#333}
.welcome em{color:var(--red);font-size:26px}
.hr{height:1px;background:var(--rule)}

/* cards */
.card{top:330px;width:142px}
.card-img{height:105px;position:relative}
.tags{position:absolute;top:0;right:0;display:flex;gap:1px}
.tags span{font-size:5px;color:#fff;background:var(--dark);padding:0 4px;line-height:14px;font-weight:600}
.tags .r{background:var(--red)}
.card h3,.feature h3{font-weight:400;color:#333}
.card h3{font-size:12.5px;margin:14px 5px 0;padding-bottom:4px;border-bottom:1px solid #d06066}
.card p{font-size:5px;line-height:6.6px;margin:8px 6px 0;color:#333}

.feature{left:314px;width:270px}
.feature h3{font-size:12.5px}
.feature p{font-size:5px;line-height:6.6px;margin-top:10px;color:#333}
.btn{display:inline-block;background:var(--red);color:#fff;font-size:7.5px;padding:0 10px;line-height:16px;border:1px solid #8d0c10}

/* bottom tiles */
.tile{top:791px;width:105px}
.tile-img{height:94px;position:relative}
.tile-img b{position:absolute;left:0;right:0;bottom:0;height:17px;background:rgba(255,255,255,.75);color:var(--red);font-weight:400;font-size:8.5px;text-align:center;line-height:17px}
.tile p{font-size:5px;line-height:6.6px;margin:9px 2px 0}
.tile .sm{position:absolute;right:2px;top:167px;font-size:5px;line-height:12px;padding:0 5px}

.signin{left:476px;top:786px;width:100px}
.signin h4{font-weight:400;color:var(--red);font-size:10px}
.field{height:9px;border:1px solid #777;border-radius:2px;background:#fff;font-size:4.5px;line-height:7px;padding-left:3px;margin-top:4px}
.signin small{display:block;font-size:5px}
.mini{display:inline-block;width:34px;height:8px;background:var(--red);border-radius:2px;vertical-align:middle}

/* footer */
.footer{left:0;top:991px;width:714px;height:209px;background:var(--dark);color:#ddd}
.f-logo{left:324px;top:13px;display:flex;align-items:center;gap:4px}
.f-logo i{width:10px;height:10px;border-radius:50%;background:var(--red)}
.f-logo span{font-size:6px;font-weight:700;color:#ddd}
.f-col{top:60px;width:98px}
.f-col h5{font-size:6px;color:#fff;padding-bottom:4px;border-bottom:1px solid #555}
.f-col p{font-size:4.6px;line-height:6.3px;margin-top:6px}
.f-col .btn{font-size:4.5px;line-height:9px;padding:0 4px;margin-top:6px}
.f-social{display:flex;gap:2px;margin-top:6px}
.f-social span{width:7px;height:7px;background:#4a78b8;border-radius:1px}
.f-nav{top:162px;left:0;width:714px;text-align:center;font-size:7.5px;color:#fff;word-spacing:3px}
.f-copy{top:183px;left:0;width:714px;text-align:center;font-size:6.2px;color:#ddd;word-spacing:2px}
</style>
</head>
<body>

<!-- header -->
<div class="abs brand"><span class="brand-dot"></span><span class="brand-name">Reel Tide Rovers</span></div>
<div class="abs social-top"><span class="badge"></span><span></span><span></span><span></span><span></span></div>
<div class="abs account">Sign Up &nbsp;|&nbsp; Log In &nbsp;|&nbsp; Checkout</div>
<div class="abs search">
  <div style="width:58px">What ?</div>
  <div style="width:58px">Find</div>
  <div style="width:48px">Near</div>
</div>

<nav class="abs nav">
  <a>Home</a><a>Lakes</a><a>RT Rovers</a><a>Blog</a><a>Directory</a><a>Equipment</a><a>Help</a>
</nav>

<!-- slider -->
<div class="abs slide s-left" role="img" aria-label="Angler in a rowboat on a misty orange lake"></div>
<div class="abs slide s-main" role="img" aria-label="Two anglers on a bass boat at sunset"></div>
<div class="abs slide s-right" role="img" aria-label="Anglers in a boat on a golden lake at dusk"></div>
<div class="abs arrow" style="left:12px"><svg width="10" height="10" viewBox="0 0 10 10"><path d="M7 1 3 5l4 4" fill="none" stroke="#333" stroke-width="2"/></svg></div>
<div class="abs arrow" style="left:681px"><svg width="10" height="10" viewBox="0 0 10 10"><path d="M3 1l4 4-4 4" fill="none" stroke="#333" stroke-width="2"/></svg></div>

<div class="abs welcome">Welcome to <em>Reel Tide</em></div>
<div class="abs hr" style="left:0;top:317px;width:714px"></div>

<!-- cards -->
<div class="abs card" style="left:138px">
  <div class="card-img" role="img" aria-label="Angler casting against a sunset" style="background:linear-gradient(#e0a44a,#7a4a18 60%,#2a1a08)">
    <div class="tags"><span class="r">16.08.2013 ▾</span><span>User</span><span>Tahoe Lake</span><span>★★★★★</span></div>
  </div>
  <h3>Newest fishing reports</h3>
  <p>Lorem ipsum dolor sit amet, consectetur adipisicing elit, sed do eiusmod tempor incididunt ut labore et dolore magna aliqua.</p>
  <p>Ut enim ad minim veniam, quis nostrud exercitation ullamco laboris nisi ut aliquip ex ea commodo consequat.</p>
</div>
<div class="abs card" style="left:286px">
  <div class="card-img" role="img" aria-label="Hand holding a rod and reel over open water" style="background:linear-gradient(#9cc3e0,#3d7aa8 45%,#1e4f7a)">
    <div class="tags"><span>User</span><span class="r">Tahoe Lake</span><span>★★★★★</span></div>
  </div>
  <h3>Newest Features</h3>
  <p>Lorem ipsum dolor sit amet, consectetur adipisicing elit, sed do eiusmod tempor incididunt ut labore et dolore magna aliqua.</p>
  <p>Ut enim ad minim veniam, quis nostrud exercitation ullamco laboris nisi ut aliquip ex ea commodo consequat.</p>
</div>
<div class="abs card" style="left:434px">
  <div class="card-img" role="img" aria-label="Fish leaping from the water near a boat" style="background:linear-gradient(#a9c4dc,#5a86ad 40%,#2f5f8a)">
    <div class="tags"><span>User</span><span class="r">Tahoe Lake</span><span>★★★★★</span></div>
  </div>
  <h3>Newest photos</h3>
  <p>Lorem ipsum dolor sit amet, consectetur adipisicing elit, sed do eiusmod tempor incididunt ut labore et dolore magna aliqua.</p>
  <p>Ut enim ad minim veniam, quis nostrud exercitation ullamco laboris nisi ut aliquip ex ea commodo consequat.</p>
</div>

<div class="abs hr" style="left:138px;top:531px;width:438px"></div>

<!-- map -->
<div class="abs" role="img" aria-label="Map of the USA and Canada by state and province" style="left:142px;top:538px;width:122px;height:120px;background:radial-gradient(ellipse at 50% 55%,#d8c49a 0%,#c9b184 55%,transparent 72%)"></div>
<div class="abs feature" style="top:548px">
  <h3>USA and Canada Map</h3>
  <p>Lorem ipsum dolor sit amet, consectetur adipisicing elit, sed do eiusmod tempor incididunt ut labore et dolore magna aliqua.</p>
  <p style="margin-top:5px">Ut enim ad minim veniam, quis nostrud exercitation ullamco laboris nisi ut aliquip ex ea commodo consequat.</p>
  <a class="btn" style="margin-top:14px">Go to States</a>
</div>

<div class="abs hr" style="left:138px;top:665px;width:438px"></div>

<!-- blog -->
<div class="abs" role="img" aria-label="Anglers standing on a boat at sunset" style="left:140px;top:678px;width:142px;height:88px;border:1px solid #999;background:linear-gradient(#6d87a8,#c4ccd4 40%,#2a3b5c 60%,#101c36)"></div>
<div class="abs feature" style="top:673px">
  <h3>Newest Blog Posts</h3>
  <p>Lorem ipsum dolor sit amet, consectetur adipisicing elit, sed do eiusmod tempor incididunt ut labore et dolore magna aliqua.</p>
  <p style="margin-top:5px">Ut enim ad minim veniam, quis nostrud exercitation ullamco laboris nisi ut aliquip ex ea commodo consequat.</p>
  <a class="btn" style="margin-top:12px">View More</a>
</div>

<div class="abs hr" style="left:138px;top:778px;width:438px"></div>

<!-- tiles -->
<div class="abs tile" style="left:140px">
  <div class="tile-img" role="img" aria-label="Close-up of a fly fishing reel" style="background:linear-gradient(#3a3f48,#9aa3ad 50%,#4b5058)"><b>Hottest Gear Section</b></div>
  <p>Lorem ipsum dolor sit amet, consectetur adipisicing elit, sed do eiusmod tempor incididunt ut labore et dolore magna aliqua.</p>
  <p style="margin-top:5px">Ut enim ad minim veniam, quis nostrud exercitation ullamco laboris nisi ut aliquip ex ea commodo consequat.</p>
  <a class="btn sm">View More</a>
</div>
<div class="abs tile" style="left:250px">
  <div class="tile-img" role="img" aria-label="Angler holding up a largemouth bass" style="background:linear-gradient(#8fb3d8,#5b3c8e 55%,#2d3a2a)"><b>In the news Section</b></div>
  <p>Lorem ipsum dolor sit amet, consectetur adipisicing elit, sed do eiusmod tempor incididunt ut labore et dolore magna aliqua.</p>
  <p style="margin-top:5px">Ut enim ad minim veniam, quis nostrud exercitation ullamco laboris nisi ut aliquip ex ea commodo consequat.</p>
  <a class="btn sm">View More</a>
</div>
<div class="abs tile" style="left:359px">
  <div class="tile-img" role="img" aria-label="Fish swimming over a rocky bottom" style="background:linear-gradient(#b8ab94,#7d7264 50%,#a0937c)"><b>Our Newsletter</b></div>
  <p>Lorem ipsum dolor sit amet, consectetur adipisicing elit, sed do eiusmod tempor incididunt ut labore et dolore magna aliqua.</p>
  <p style="margin-top:5px">Ut enim ad minim veniam, quis nostrud exercitation ullamco laboris nisi ut aliquip ex ea commodo consequat.</p>
  <a class="btn sm">View More</a>
</div>

<div class="abs signin">
  <h4>Sign in and Register</h4>
  <div class="field" style="margin-top:20px">lorem@ipsum.com</div>
  <div class="field">•••••••••••••••</div>
  <small style="margin-top:3px">☐ Remember me</small>
  <div style="margin-top:3px"><span class="mini"></span> <i style="color:var(--red);font-size:8px;margin:0 9px">or</i> <span class="mini"></span></div>
  <small style="margin-top:4px">Forgot account details ?</small>
</div>

<!-- footer -->
<footer class="abs footer">
  <div class="abs f-logo"><i></i><span>Reel Tide Rovers</span></div>
  <div class="abs hr" style="left:138px;top:29px;width:438px;background:#666"></div>

  <div class="abs f-col" style="left:146px">
    <h5>Reel Tide</h5>
    <p>Lorem ipsum dolor sit amet, consectetur adipiscing elit. Sed blandit massa vel mauris sollicitudin dignissim. Phasellus ultrices tellus eget ipsum ornare molestie scelerisque eros dignissim.</p>
    <a class="btn">Read more</a>
  </div>
  <div class="abs f-col" style="left:253px">
    <h5>About Us</h5>
    <p>Lorem ipsum dolor sit amet, consectetur adipiscing elit. Sed blandit massa vel mauris sollicitudin dignissim. Phasellus ultrices tellus eget ipsum ornare molestie.</p>
    <a class="btn">Read more</a>
  </div>
  <div class="abs f-col" style="left:360px">
    <h5>Contact Us</h5>
    <p>Lorem ipsum dolor sit amet, consectetur adipiscing elit.</p>
    <p>Lorem ipsum dolor sit amet, consectetur adipiscing elit.</p>
  </div>
  <div class="abs f-col" style="left:467px">
    <h5>Social Media</h5>
    <div class="f-social"><span></span><span></span><span></span><span></span><span style="background:#c23a2b"></span></div>
  </div>

  <div class="abs f-nav">Home | About Us | Lakes | RT Rovers | Blog | Directory | Equipment | Help | Contact Us</div>
  <div class="abs hr" style="left:138px;top:175px;width:438px;background:#777"></div>
  <div class="abs f-copy">Copyright 2013 Reel Tide | Terms and Conditions | Sitemap | Site by Reel Tide</div>
</footer>

</body>
</html>
```